Sunny Trails and joy Business card

I have a logo, but will like a business card design. Is for a travel agency in Mexico. We focus in family experiences.

I will liek some thing different and unique, from the traditional business card, something to get remmeber for.

Business card information:

Leandro R. Quiroga
leandro@sunnytrailsjoy.example

Alameda 742, 3 piso
Col. Tepalcatl
Mexico, D.F. 04910

office: (55) 4821-7390
mobile: (55) 7034-1258

www.sunnytrailsjoy.example
@sunnytjoy
blog: sunnytrailsandjoy.blog.example
facebook: SunnyTrailsAndJoy

```html
<!DOCTYPE html>
<html lang="es">
<head>
<meta charset="utf-8">
<title>Sunny Trails and joy — Business card</title>
<link rel="stylesheet" href="https://fonts.googleapis.com/css2?family=Source+Sans+3:wght@400;600;700&display=swap">
<style>
  :root {
    --backdrop: #e9e6e1;
    --card: #ffffff;
    --brand-blue: #1f5f8f;
    --ink: #3a3a3a;
    --ink-soft: #555555;
    --accent-circle: #cfe3f2;
    --shadow: rgba(0, 0, 0, 0.28);
  }
  * { box-sizing: border-box; margin: 0; padding: 0; }
  html, body {
    width: 1200px;
    height: 511px;
    overflow: hidden;
    background: var(--backdrop);
    font-family: "Source Sans 3", "Myriad Pro", Arial, sans-serif;
  }
  .canvas { position: relative; width: 1200px; height: 511px; }
  .card {
    position: absolute;
    top: 109px;
    width: 516px;
    height: 294px;
    background: var(--card);
    box-shadow: 0 3px 6px var(--shadow);
  }
  .card--front { left: 68px; }
  .card--back { left: 618px; }

  .brand {
    position: absolute;
    display: flex;
    align-items: center;
    gap: 10px;
    color: var(--brand-blue);
    font-weight: 700;
    font-size: 30px;
    line-height: 1;
  }
  .brand__dot {
    width: 34px; height: 34px;
    border-radius: 50%;
    background: var(--accent-circle);
    flex: none;
  }
  .card--front .brand { left: 22px; top: 92px; }
  .card--back .brand { left: 0; right: 0; top: 110px; justify-content: center; }

  .edge-bar {
    position: absolute;
    width: 6px;
    background: var(--brand-blue);
  }
  .edge-bar--left { left: 0; top: 188px; height: 36px; }
  .edge-bar--right { right: 0; top: 188px; height: 96px; }

  .holder {
    position: absolute;
    left: 24px; top: 187px;
    color: var(--brand-blue);
    font-weight: 700;
    font-size: 18px;
  }
  .contact-list {
    position: absolute;
    right: 20px; top: 187px;
    list-style: none;
    text-align: right;
    color: var(--ink-soft);
    font-size: 13.5px;
    line-height: 17.5px;
  }
  .contact-list li { display: flex; justify-content: flex-end; align-items: center; gap: 7px; }
  .contact-list svg { width: 11px; height: 11px; fill: var(--brand-blue); flex: none; }
  .address {
    position: absolute;
    right: 22px; top: 263px;
    color: var(--ink);
    font-size: 14px;
  }

  .social-list {
    position: absolute;
    left: 0; right: 0; top: 183px;
    list-style: none;
    color: var(--ink);
    font-size: 14.5px;
  }
  .social-list li { display: flex; justify-content: center; align-items: center; gap: 8px; height: 22px; margin-bottom: 16px; }
  .social-list .badge { width: 20px; height: 20px; border-radius: 3px; background: var(--brand-blue); flex: none; }
</style>
</head>
<body>
<main class="canvas">
  <section class="card card--front" aria-label="Front of business card">
    <div class="brand"><span class="brand__dot"></span><span>Sunny Trails<br>and joy</span></div>
    <span class="edge-bar edge-bar--left"></span>
    <span class="edge-bar edge-bar--right"></span>
    <p class="holder">Leandro R. Quiroga</p>
    <ul class="contact-list">
      <li>(55) 4821-7390
        <svg viewBox="0 0 12 12" aria-hidden="true"><path d="M2.5 1 4.5 1 5.3 3.5 4 4.6C4.7 6 6 7.3 7.4 8L8.5 6.7 11 7.5 11 9.5C11 10.3 10.3 11 9.5 11 5 11 1 7 1 2.5 1 1.7 1.7 1 2.5 1Z"/></svg></li>
      <li>(55) 7034-1258
        <svg viewBox="0 0 12 12" aria-hidden="true"><path d="M3.5 0.5h5a1 1 0 0 1 1 1v9a1 1 0 0 1-1 1h-5a1 1 0 0 1-1-1v-9a1 1 0 0 1 1-1Zm0.6 1.5v6h3.8v-6Zm1.9 7a0.7 0.7 0 1 0 0 1.4 0.7 0.7 0 0 0 0-1.4Z"/></svg></li>
      <li>leandro@sunnytrailsjoy.example
        <svg viewBox="0 0 12 12" aria-hidden="true"><path d="M1 3h10v7H1Zm1 1 4 3 4-3Z" fill-rule="evenodd"/></svg></li>
      <li>www.sunnytrailsjoy.example
        <svg viewBox="0 0 12 12" aria-hidden="true"><circle cx="6" cy="6" r="5"/><path d="M1 6h10" stroke="#fff" stroke-width="1"/></svg></li>
    </ul>
    <p class="address">Alameda 742, 3 piso, Col. Tepalcatl Mexico, D.F. 04910</p>
  </section>

  <section class="card card--back" aria-label="Back of business card">
    <div class="brand"><span class="brand__dot"></span><span>Sunny Trails<br>and joy</span></div>
    <ul class="social-list">
      <li><span class="badge"></span>sunnytrailsandjoy.blog.example</li>
      <li><span class="badge"></span>SunnyTrailsAndJoy</li>
    </ul>
  </section>
</main>
</body>
</html>
```